The Hollowreed Project WEBSITE DESIGN

Hollowreed is a not for profit working in international aid and development. The website needs to be lively not depressing,earthy rather than bling, have a dramatic impact over lightweight. It may be that a black and white with spot colour may be more impacting given the simplicity I want for the site. Hollowreed works in partnership with registered NGOs in Asia and Africa. At any one time it will have about five feature projects. The purpose is for people to be able to find out about the projects, the countries, the partner organisations, people's stories and then give people the opportunity to give their financial and volunteer support.

Target Market(s)

First World Donors
All ages but particularly 25 - 55

Industry/Entity Type

Human Rights

Number of Pages Required

5+ page

Font styles to use
Sans Serif

Requirements
Must have
• Simplicity
• Easy access to giving options
• Highlight stories both video and image + copy (sample in attachments)
• Lots of images over copy
Nice to have
• Interest
• Not boring
• May work in black and white with a spot colour or sepia look
Should not have
• Shiny new look
• Dont know how many pages or if it be coded or uncoded - makes no sense to me

```html
<!DOCTYPE html>
<html lang="en">
<head>
<meta charset="utf-8">
<title>The Hollowreed Project</title>
<link href="https://fonts.googleapis.com/css2?family=Open+Sans:wght@400;600;700&family=Lora:wght@400;700&display=swap" rel="stylesheet">
<style>
:root{
  --blue:#3aa6dd;
  --blue-dark:#1d8ccc;
  --orange:#f6a623;
  --orange-dark:#e8901a;
  --ink:#333;
  --muted:#777;
  --grey-bg:#f0f0f0;
  --footer:#2a2a2a;
  --footer-line:#3d3d3d;
  --white:#fff;
}
*{box-sizing:border-box;margin:0;padding:0}
html,body{width:1200px;height:2832px;overflow:hidden}
body{font-family:'Open Sans',sans-serif;color:var(--ink);background:var(--white);position:relative}
.btn{display:inline-block;background:var(--orange);color:var(--white);font-weight:700;text-transform:uppercase;font-size:15px;padding:10px 24px;border-radius:2px}
.btn-blue{background:var(--blue-dark)}

/* hero */
.hero{position:absolute;left:0;top:0;width:1200px;height:512px}
.hero-photo{position:absolute;inset:0;background:linear-gradient(180deg,#6d8fb0 0%,#c9d3dc 35%,#e9ecef 55%,#8f949a 100%)}
.hero-shade{position:absolute;left:0;right:0;bottom:0;height:200px;background:linear-gradient(180deg,rgba(0,0,0,0),rgba(0,0,0,.55))}
.brand-box{position:absolute;left:8px;top:0;width:94px;height:112px;background:#111;display:flex;flex-direction:column;align-items:center;justify-content:center;gap:8px}
.brand-dot{width:34px;height:34px;border-radius:50%;background:var(--orange)}
.brand-name{color:var(--white);font-size:13px;font-weight:700}
.topnav{position:absolute;right:0;top:0;width:860px;height:38px;background:rgba(20,20,20,.9);display:flex;align-items:center;justify-content:flex-end;padding-right:12px;gap:0}
.topnav a{color:var(--white);font-size:14px;text-decoration:none;padding:0 14px;border-right:1px solid #555}
.topnav a.active{color:var(--orange)}
.topnav .btn{margin-left:14px;font-size:13px;padding:7px 14px;border-radius:2px}
.slide-arrow{position:absolute;top:270px;width:30px;height:40px;background:rgba(0,0,0,.6);display:flex;align-items:center;justify-content:center}
.slide-arrow.left{left:0}.slide-arrow.right{right:0}
.hero-title{position:absolute;left:0;right:0;top:398px;text-align:center;color:var(--white);font-size:27px;font-weight:600;text-shadow:0 2px 4px rgba(0,0,0,.5)}
.hero-cta{position:absolute;left:50%;top:450px;transform:translateX(-50%);text-transform:none;font-size:17px;padding:10px 26px;display:flex;align-items:center;gap:10px}

/* service band */
.services{position:absolute;left:0;top:512px;width:1200px;height:288px;background:var(--blue);display:flex;justify-content:center;gap:118px;padding-top:62px}
.service{display:flex;flex-direction:column;align-items:center;gap:28px}
.service-ring{width:140px;height:140px;border-radius:50%;background:rgba(255,255,255,.25);display:flex;align-items:center;justify-content:center}
.service-disc{width:112px;height:112px;border-radius:50%;background:var(--white);display:flex;align-items:center;justify-content:center}
.service-label{color:var(--white);font-weight:700;font-size:16px;letter-spacing:.5px}

/* welcome */
.welcome{position:absolute;left:0;top:800px;width:1200px;height:290px;padding:30px 40px 0 28px;display:flex;gap:40px}
.welcome-copy{width:620px}
.welcome h2{font-family:'Lora',serif;font-weight:400;font-size:26px;margin-bottom:12px}
.welcome p{font-size:13px;line-height:1.65;color:var(--muted)}
.read-more{display:inline-block;margin-top:14px;font-size:13px;font-weight:700;color:var(--ink)}
.video{position:relative;width:472px;height:240px;background:linear-gradient(135deg,#cdd3d8,#8f8a84 55%,#5b5d63);margin-top:-6px}
.video-bar{position:absolute;left:0;right:0;bottom:0;height:26px;background:rgba(0,0,0,.75);display:flex;align-items:center;padding:0 10px;gap:10px}
.video-track{flex:1;height:4px;background:#666}
.video-track span{display:block;width:30%;height:4px;background:#e33}

/* about band */
.about-band{position:absolute;left:0;top:1096px;width:1200px;height:190px;background:linear-gradient(90deg,var(--orange),#f8b547 50%,var(--orange));display:flex;align-items:center;padding-left:60px}
.about-brand{display:flex;flex-direction:column;align-items:center;gap:6px;width:140px}
.about-brand .brand-dot{width:56px;height:56px;background:#3b3b3b}
.about-brand .brand-name{color:#3b3b3b;font-size:16px}
.about-links{display:flex;gap:92px;margin-left:60px}
.about-link{display:flex;flex-direction:column;align-items:center;gap:12px}
.about-ring{width:96px;height:96px;border-radius:50%;border:3px solid rgba(255,255,255,.8);display:flex;align-items:center;justify-content:center}
.about-label{color:#3b3b3b;font-size:16px}

/* projects */
.projects{position:absolute;left:0;top:1290px;width:1200px;height:300px}
.section-title{font-family:'Lora',serif;font-weight:400;font-size:26px;text-align:center}
.projects .section-title{margin-top:20px}
.title-rule{width:280px;height:1px;background:#ccc;margin:8px auto 0}
.project-cards{display:flex;justify-content:center;gap:16px;margin-top:20px}
.project{width:282px}
.project-photo{position:relative;height:150px}
.project-place{position:absolute;left:10px;bottom:8px;color:var(--white);font-family:'Lora',serif;font-size:20px;text-shadow:0 1px 3px rgba(0,0,0,.7)}
.project-caption{background:#eee;font-size:13px;padding:8px 10px;height:54px;line-height:1.4}

/* stories */
.stories{position:absolute;left:0;top:1596px;width:1200px;height:394px;background:var(--grey-bg);display:flex;gap:40px;padding:28px 40px 0 60px}
.stories-col{width:520px}
.col-head{display:flex;align-items:center;gap:10px;font-family:'Lora',serif;font-size:25px;margin-bottom:20px}
.col-head .rule{flex:1;height:1px;background:#ccc}
.story{display:flex;gap:16px;margin-bottom:18px}
.story-thumb{width:108px;height:80px;flex:none}
.story-text{font-size:12px;line-height:1.55;color:var(--muted)}
.story-date{color:var(--orange-dark);font-weight:600}
.article{display:flex;gap:10px;margin-bottom:16px;font-size:12px;line-height:1.55;color:var(--muted)}
.article b{color:var(--ink)}

/* giving */
.giving{position:absolute;left:0;top:1996px;width:1200px;height:270px;display:flex;justify-content:center;gap:42px;padding-top:28px}
.give-card{position:relative;width:448px;height:232px;display:flex;flex-direction:column;align-items:center;justify-content:center;color:var(--white);text-align:center}
.give-card::after{content:"";position:absolute;inset:0;background:rgba(0,0,0,.35)}
.give-card>*{position:relative;z-index:1}
.give-card h3{font-size:34px;font-weight:400;margin-bottom:6px}
.give-card p{font-size:12px;width:300px;line-height:1.5;margin-bottom:14px}
.give-bg{position:absolute;inset:0}

/* cta strip */
.cta-strip{position:absolute;left:0;top:2286px;width:1200px;height:76px;background:var(--orange);display:flex;align-items:center;padding:0 60px 0 40px;justify-content:space-between}
.cta-strip p{color:var(--white);font-weight:700;font-size:19px;line-height:1.3;width:760px}
.cta-strip .btn{font-size:22px;padding:12px 30px}

/* footer */
.footer{position:absolute;left:0;top:2380px;width:1200px;height:396px;background:var(--footer);color:#ccc}
.footer-nav{display:flex;justify-content:center;padding:30px 0 26px;border-bottom:1px solid var(--footer-line)}
.footer-nav a{color:#ddd;font-size:14px;text-decoration:none;padding:0 14px;border-right:1px solid #555}
.footer-nav a:last-child{border-right:none}
.footer-cols{display:flex;gap:40px;padding:22px 40px 0 60px}
.footer-col{width:340px}
.footer-col h4{color:var(--white);font-size:14px;font-weight:700;text-transform:uppercase;margin-bottom:14px}
.footer-col p{font-size:13px;line-height:1.6}
.contact-line{display:flex;align-items:center;gap:10px;font-size:13px;margin-top:8px}
.map{width:300px;height:180px;background:linear-gradient(135deg,#e8e4dc,#d6d9cf)}
.signup{display:flex;flex-direction:column;gap:10px;margin-top:12px}
.signup .field{height:36px;background:var(--white);color:#999;font-size:13px;padding:9px 10px;width:260px}
.signup .btn{width:110px;text-align:center;background:var(--blue)}

/* bottom bar */
.bottom-bar{position:absolute;left:0;top:2776px;width:1200px;height:56px;background:var(--blue-dark);display:flex;align-items:center;padding:0 40px 0 60px;color:var(--white);font-size:13px}
.pay-badge{width:86px;height:30px;background:#f3c43a;border-radius:4px;margin-left:300px}
.socials{display:flex;gap:14px;margin-left:auto}
.socials span{width:22px;height:22px;border-radius:50%;background:rgba(255,255,255,.85)}
</style>
</head>
<body>

<header class="hero">
  <div class="hero-photo" role="img" aria-label="Photo of volunteers in white shirts stacking hands together"></div>
  <div class="hero-shade"></div>
  <div class="brand-box"><span class="brand-dot"></span><span class="brand-name">Hollowreed</span></div>
  <nav class="topnav">
    <a href="#">Home</a><a href="#">About Hollowreed</a><a href="#" class="active">Projects</a><a href="#">News / Stories</a><a href="#" style="border-right:none">Contact Us</a>
    <span class="btn">Donate Now</span>
  </nav>
  <div class="slide-arrow left"><svg width="12" height="16" viewBox="0 0 12 16"><path d="M9 2L3 8l6 6" stroke="#fff" stroke-width="2" fill="none"/></svg></div>
  <div class="slide-arrow right"><svg width="12" height="16" viewBox="0 0 12 16"><path d="M3 2l6 6-6 6" stroke="#fff" stroke-width="2" fill="none"/></svg></div>
  <h1 class="hero-title">We Are A Not For Profit Working In International Aid And Development</h1>
  <span class="btn hero-cta"><svg width="20" height="20" viewBox="0 0 20 20"><circle cx="10" cy="10" r="9" fill="none" stroke="#fff" stroke-width="2"/><path d="M8 6l4 4-4 4" stroke="#fff" stroke-width="2" fill="none"/></svg>Get Started With Us</span>
</header>

<section class="services">
  <div class="service"><div class="service-ring"><div class="service-disc"><svg width="48" height="48" viewBox="0 0 48 48"><rect x="10" y="6" width="28" height="36" rx="2" fill="none" stroke="#3aa6dd" stroke-width="3"/><path d="M16 16h16M16 24h16M16 32h10" stroke="#3aa6dd" stroke-width="3"/></svg></div></div><span class="service-label">ENROLL</span></div>
  <div class="service"><div class="service-ring"><div class="service-disc"><svg width="48" height="48" viewBox="0 0 48 48"><circle cx="24" cy="16" r="9" fill="#3aa6dd"/><path d="M8 42c0-10 7-15 16-15s16 5 16 15z" fill="#3aa6dd"/></svg></div></div><span class="service-label">VOLUNTEER</span></div>
  <div class="service"><div class="service-ring"><div class="service-disc"><svg width="48" height="48" viewBox="0 0 48 48"><path d="M24 42L8 26a9 9 0 0116-12 9 9 0 0116 12z" fill="#3aa6dd"/></svg></div></div><span class="service-label">SUPPORT</span></div>
  <div class="service"><div class="service-ring"><div class="service-disc"><svg width="48" height="48" viewBox="0 0 48 48"><circle cx="34" cy="12" r="6" fill="#3aa6dd"/><circle cx="14" cy="24" r="6" fill="#3aa6dd"/><circle cx="34" cy="36" r="6" fill="#3aa6dd"/><path d="M34 12L14 24l20 12" stroke="#3aa6dd" stroke-width="3" fill="none"/></svg></div></div><span class="service-label">SHARE</span></div>
</section>

<section class="welcome">
  <div class="welcome-copy">
    <h2>Welcome to Hollowreed Projects</h2>
    <p>We partner with registered local organisations across Asia and Africa to support communities with practical, lasting help. Each project is chosen together with the people it serves, so that schools, clinics, gardens and small businesses grow from what a village already knows it needs. Our supporters follow every project from its first season to its last report, and see where each gift goes.</p>
    <p style="margin-top:8px">Volunteers, donors and partners share one simple aim: fair chances for families to build their own future. Read the stories below, meet our partner organisations and find a way to join in that suits you.</p>
    <span class="read-more">Read More</span>
  </div>
  <div class="video" role="img" aria-label="Video still of a small team meeting around a table">
    <div class="video-bar"><svg width="12" height="12" viewBox="0 0 12 12"><path d="M2 1l9 5-9 5z" fill="#fff"/></svg><div class="video-track"><span></span></div><svg width="14" height="12" viewBox="0 0 14 12"><path d="M1 4h3l4-3v10L4 8H1z" fill="#fff"/></svg></div>
  </div>
</section>

<section class="about-band">
  <div class="about-brand"><span class="brand-dot"></span><span class="brand-name">Hollowreed</span></div>
  <div class="about-links">
    <div class="about-link"><div class="about-ring"><svg width="44" height="44" viewBox="0 0 44 44"><circle cx="22" cy="22" r="16" fill="none" stroke="#3b3b3b" stroke-width="3"/><circle cx="22" cy="22" r="8" fill="none" stroke="#3b3b3b" stroke-width="3"/><circle cx="22" cy="22" r="2" fill="#3b3b3b"/></svg></div><span class="about-label">Purpose</span></div>
    <div class="about-link"><div class="about-ring"><svg width="44" height="44" viewBox="0 0 44 44"><path d="M22 6l4.5 10 11 1-8.3 7.3 2.5 10.7L22 29.5 12.3 35l2.5-10.7L6.5 17l11-1z" fill="none" stroke="#3b3b3b" stroke-width="3"/></svg></div><span class="about-label">Values</span></div>
    <div class="about-link"><div class="about-ring"><svg width="44" height="44" viewBox="0 0 44 44"><rect x="8" y="10" width="28" height="24" rx="2" fill="none" stroke="#3b3b3b" stroke-width="3"/><path d="M14 18h16M14 25h10" stroke="#3b3b3b" stroke-width="3"/></svg></div><span class="about-label">Meaning of Name</span></div>
    <div class="about-link"><div class="about-ring"><svg width="44" height="44" viewBox="0 0 44 44"><circle cx="15" cy="16" r="6" fill="#3b3b3b"/><circle cx="29" cy="16" r="6" fill="#3b3b3b"/><path d="M4 36c0-7 5-11 11-11s11 4 11 11zM18 36c0-7 5-11 11-11s11 4 11 11z" fill="#3b3b3b"/></svg></div><span class="about-label">Board</span></div>
  </div>
</section>

<section class="projects">
  <h2 class="section-title">Our Current Projects</h2>
  <div class="title-rule"></div>
  <div class="project-cards">
    <div class="project"><div class="project-photo" role="img" aria-label="Photo of children in a classroom" style="background:linear-gradient(135deg,#9c8a6a,#5f6f58)"><span class="project-place">Kratie Cambodia</span></div><div class="project-caption">Children's Home Offering Cooperative Shelter And Rural School Support</div></div>
    <div class="project"><div class="project-photo" role="img" aria-label="Photo of a village women's group" style="background:linear-gradient(135deg,#7a6a5a,#b29a72)"><span class="project-place">Northern Rwanda</span></div><div class="project-caption">Women's Self Help Groups In Rural Rwanda</div></div>
    <div class="project"><div class="project-photo" role="img" aria-label="Photo of women at a community meeting" style="background:linear-gradient(135deg,#a27a5c,#6a5442)"><span class="project-place">Coastal Kenya</span></div><div class="project-caption">Coaching Women NGO Leaders From Around The Country</div></div>
  </div>
</section>

<section class="stories">
  <div class="stories-col">
    <div class="col-head"><svg width="30" height="26" viewBox="0 0 30 26"><path d="M2 2h26v16H12l-6 6v-6H2z" fill="#3aa6dd"/></svg>Ongoing stories<span class="rule"></span></div>
    <div class="story"><div class="story-thumb" role="img" aria-label="Photo of a smiling student" style="background:linear-gradient(135deg,#8b6c50,#c9a77d)"></div><div class="story-text"><span class="story-date">School term opens, 14th Sep 2019.</span> Twelve new pupils joined the village school this week after the harvest, with uniforms and books shared by our partner team.</div></div>
    <div class="story"><div class="story-thumb" role="img" aria-label="Photo of a mother holding a child" style="background:linear-gradient(135deg,#6f5b46,#a88f72)"></div><div class="story-text"><span class="story-date">New well finished, 02nd Sep 2019.</span> Families in the valley now walk ten minutes for clean water instead of two hours, thanks to a local builders' group.</div></div>
    <div class="story"><div class="story-thumb" role="img" aria-label="Photo of women working in a field" style="background:linear-gradient(135deg,#7d7050,#b7a877)"></div><div class="story-text"><span class="story-date">Garden harvest, 21st Aug 2019.</span> The women's group sold its first vegetable crop at market and agreed to save part of the profit for seed.</div></div>
  </div>
  <div class="stories-col">
    <div class="col-head"><svg width="28" height="28" viewBox="0 0 28 28"><rect x="3" y="3" width="22" height="22" rx="2" fill="none" stroke="#3aa6dd" stroke-width="3"/><path d="M8 20l2-6 8-8 4 4-8 8z" fill="#3aa6dd"/></svg>Articles About Aid &amp; Development<span class="rule"></span></div>
    <div class="article"><svg width="14" height="14" viewBox="0 0 14 14" style="flex:none;margin-top:2px"><path d="M2 7l3 3 7-7" stroke="#3aa6dd" stroke-width="2.5" fill="none"/></svg><span><b>Local first aid.</b> Why projects led by local partners last longer, and what donors can learn from them about patience.</span></div>
    <div class="article"><svg width="14" height="14" viewBox="0 0 14 14" style="flex:none;margin-top:2px"><path d="M2 7l3 3 7-7" stroke="#3aa6dd" stroke-width="2.5" fill="none"/></svg><span><b>Small loans, big steps.</b> How savings groups help women start small trades and keep their children in school.</span></div>
    <div class="article"><svg width="14" height="14" viewBox="0 0 14 14" style="flex:none;margin-top:2px"><path d="M2 7l3 3 7-7" stroke="#3aa6dd" stroke-width="2.5" fill="none"/></svg><span><b>Water and health.</b> A short guide to how clean water changes school attendance and family health in rural areas.</span></div>
    <div class="article"><svg width="14" height="14" viewBox="0 0 14 14" style="flex:none;margin-top:2px"><path d="M2 7l3 3 7-7" stroke="#3aa6dd" stroke-width="2.5" fill="none"/></svg><span><b>Giving well.</b> Questions to ask before you give, and how we report back on every project each year.</span></div>
  </div>
</section>

<section class="giving">
  <div class="give-card"><div class="give-bg" role="img" aria-label="Photo of hands holding coins" style="background:linear-gradient(135deg,#8a7a64,#4f4a44)"></div><h3>Online Giving</h3><p>Give once or every month and follow the project your gift supports through our regular updates.</p><span class="btn btn-blue">Donate Now</span></div>
  <div class="give-card"><div class="give-bg" role="img" aria-label="Photo of volunteers working together outdoors" style="background:linear-gradient(135deg,#6f7f8a,#4a4f57)"></div><h3>Volunteer Vacancies</h3><p>Share your time and skills with our partner teams at home or abroad, for a few weeks or longer.</p><span class="btn btn-blue">Join Now</span></div>
</section>

<section class="cta-strip">
  <p>Every gift reaches a partner project on the ground, so families can build safer, healthier lives on their own terms.</p>
  <span class="btn btn-blue">Donate Now</span>
</section>

<footer class="footer">
  <nav class="footer-nav"><a href="#">Home</a><a href="#">About Hollowreed</a><a href="#">Projects</a><a href="#">News / Stories</a><a href="#">Contact Us</a></nav>
  <div class="footer-cols">
    <div class="footer-col">
      <h4>Contact Information</h4>
      <p style="color:var(--orange)">Hollowreed Project Inc.</p>
      <p>Street Name City Name<br>State Zipcode</p>
      <div class="contact-line"><svg width="14" height="14" viewBox="0 0 14 14"><path d="M3 1l3 3-2 2a8 8 0 004 4l2-2 3 3-2 2C5 13 1 9 1 3z" fill="#3aa6dd"/></svg>(123) 456-7890</div>
      <div class="contact-line"><svg width="14" height="14" viewBox="0 0 14 14"><rect x="2" y="1" width="10" height="12" rx="1" fill="#3aa6dd"/></svg>(123) 456-7891</div>
      <div class="contact-line"><svg width="14" height="14" viewBox="0 0 14 14"><rect x="1" y="3" width="12" height="9" fill="none" stroke="#3aa6dd" stroke-width="1.5"/><path d="M1 3l6 5 6-5" stroke="#3aa6dd" stroke-width="1.5" fill="none"/></svg>info@hollowreedproject.org</div>
    </div>
    <div class="footer-col">
      <h4>Location Map</h4>
      <div class="map" role="img" aria-label="Street map showing the office location"></div>
    </div>
    <div class="footer-col">
      <h4>Newsletter Signup</h4>
      <p>Get project news and stories from the field once a month, straight to your inbox.</p>
      <div class="signup"><div class="field">Enter your email here</div><span class="btn">Submit</span></div>
    </div>
  </div>
</footer>

<div class="bottom-bar">
  <span>Copyright © 2019 Hollowreed Project. All rights reserved.</span>
  <span class="pay-badge"></span>
  <div class="socials"><span></span><span></span><span></span><span></span></div>
</div>

</body>
</html>
```